Computer repair shop

A card with our logo. And number and email and address. Our colors are baby /light blue and gray

Prefferably one sode with full logo - interested in other designs and options

Computer / mac repair shop
On site support
Snall business IT support

```html
<!DOCTYPE html>
<html lang="en">
<head>
<meta charset="utf-8">
<title>Byte Fixers – Business Card</title>
<link rel="stylesheet" href="https://fonts.googleapis.com/css2?family=Open+Sans:wght@400;600;800&display=swap">
<style>
  :root {
    --stage: #d9dcdf;
    --card: #ffffff;
    --ink: #1b1b1b;
    --text: #2a2a2a;
    --accent: #2b9ad8;
    --mascot-blue: #5aa6e0;
    --mascot-gray: #c9ccd0;
  }
  * { box-sizing: border-box; margin: 0; padding: 0; }
  html, body {
    width: 1200px; height: 800px; overflow: hidden;
    background: var(--stage);
    font-family: "Open Sans", Arial, sans-serif;
  }
  .stage {
    width: 1200px; height: 800px;
    display: flex; align-items: center; justify-content: center; gap: 40px;
  }
  .card {
    position: relative;
    width: 540px; height: 309px;
    background: var(--card);
    box-shadow: 0 6px 18px rgba(0,0,0,0.18);
  }
  .wordmark {
    color: var(--ink);
    font-weight: 800;
    letter-spacing: -1px;
    line-height: 1;
    white-space: nowrap;
  }
  .mascot {
    position: absolute;
    border-radius: 14px;
    background: linear-gradient(160deg, var(--mascot-blue), #3d86c6 70%, var(--mascot-gray));
  }

  /* front */
  .card--front .wordmark {
    position: absolute; left: 88px; top: 112px; font-size: 46px;
  }
  .card--front .mascot {
    left: 372px; top: 62px; width: 120px; height: 130px;
  }
  .services {
    position: absolute; left: 0; right: 0; bottom: 42px;
    text-align: center; font-size: 13px; color: var(--text);
  }
  .services .sep { color: var(--accent); padding: 0 4px; }

  /* back */
  .card--back .wordmark {
    position: absolute; left: 34px; top: 32px; font-size: 30px;
  }
  .person { position: absolute; left: 42px; top: 90px; }
  .person__name { color: var(--accent); font-size: 19px; font-weight: 600; }
  .person__role { color: var(--text); font-size: 14px; margin-top: -2px; }
  .contact {
    position: absolute; left: 42px; top: 152px;
    list-style: none; font-size: 14.5px; color: var(--text); line-height: 1.35;
  }
  .contact li { display: flex; align-items: center; gap: 6px; }
  .contact svg { width: 13px; height: 13px; flex: none; }
  .card--back .mascot {
    left: 372px; top: 148px; width: 130px; height: 140px;
  }
</style>
</head>
<body>
<main class="stage">
  <section class="card card--front">
    <div class="wordmark">Byte Fixers</div>
    <div class="mascot" role="img" aria-label="Cartoon computer monitor mascot holding up a finger and a screwdriver"></div>
    <p class="services">Computer / mac repair shop<span class="sep">|</span>On site support<span class="sep">|</span>Snall business IT support</p>
  </section>

  <section class="card card--back">
    <div class="wordmark">Byte Fixers</div>
    <div class="person">
      <p class="person__name">Daniel Porter</p>
      <p class="person__role">Owner</p>
    </div>
    <ul class="contact">
      <li>4820 NE Cedar Ave #112</li>
      <li>Renton WA 98056</li>
      <li>
        <svg viewBox="0 0 16 16" aria-hidden="true"><path fill="#2b9ad8" d="M3.6 1.5l2.2 2.6-1.3 1.6a9 9 0 0 0 5.8 5.8l1.6-1.3 2.6 2.2-1.5 2A11.5 11.5 0 0 1 1.5 3z"/></svg>
        +1 (555) 204-3187
      </li>
      <li>
        <svg viewBox="0 0 16 16" aria-hidden="true"><rect x="1.5" y="3.5" width="13" height="9" fill="none" stroke="#2b9ad8" stroke-width="1.4"/><path d="M1.5 3.5l6.5 5 6.5-5" fill="none" stroke="#2b9ad8" stroke-width="1.4"/></svg>
        daniel@bytefixers.com
      </li>
      <li>
        <svg viewBox="0 0 16 16" aria-hidden="true"><g fill="none" stroke="#2b9ad8" stroke-width="1.2"><circle cx="8" cy="8" r="6.5"/><ellipse cx="8" cy="8" rx="3" ry="6.5"/><path d="M1.5 8h13M2.5 5h11M2.5 11h11"/></g></svg>
        www.bytefixers.com
      </li>
    </ul>
    <div class="mascot" role="img" aria-label="Cartoon computer monitor mascot holding up a finger and a screwdriver"></div>
  </section>
</main>
</body>
</html>
```